Property investor needs a business card with logo

I need a business card for a UK based business called 'Bright Door Homes'. I buy houses quickly that is either hard to sell or people have been having trouble to sell. I then create the opportunity for people to buy houses that normally can't. This could be because they have little or no deposit saved up or they don't qualify for a mortgage. The design is to be bright so that it stands out but non threatening and basic. Yellow for the bass colour. The logo to be very simple and represent a house. It could include words like "cant sell? I'll buy it!!" or "Need a quick sale? Let me help" or something as simple as "I buy houses!!" The final design should communicate that I am not some big corporate person that is better that them, but someone that is just a person trying to help them with their situation. with a picture of me with the background removed.
Target Market(s)
Normal everyday people
Industry/Entity Type
Business
Contact Information for Business Card
Derek Pallister
07845619027
brightdoorhomes@mailbox.example
Font styles to use
Other font styles liked:
- something that looks hand written
Look and feel

```html
<!DOCTYPE html>
<html lang="en">
<head>
<meta charset="utf-8">
<title>Bright Door Homes – Business Card</title>
<link rel="stylesheet" href="https://fonts.googleapis.com/css2?family=Pinyon+Script&family=Source+Sans+3:wght@400&family=Questrial&display=swap">
<style>
  :root {
    --backdrop: #d9d4cc;
    --card-light: #f4f4f4;
    --card-mid: #cfcfcf;
    --card-edge: #b9b9b9;
    --ink: #1a1a1a;
    --ink-soft: #4a4a4a;
    --brand-yellow: #ffe600;
    --brand-black: #111111;
    --photo-dark: #2b3444;
    --photo-mid: #8a7566;
  }
  * { margin: 0; padding: 0; box-sizing: border-box; }
  html, body { width: 1083px; height: 1200px; overflow: hidden; }
  body { background: var(--backdrop); position: relative; }

  .card {
    position: absolute;
    width: 839px;
    height: 481px;
    border-radius: 32px;
    overflow: hidden;
    background: radial-gradient(ellipse at 45% 45%, var(--card-light) 0%, #e2e2e2 45%, var(--card-mid) 80%, var(--card-edge) 100%);
  }
  .card--front { left: 106px; top: 83px; }
  .card--back  { left: 119px; top: 636px; }

  .accent {
    position: absolute;
  }
  .accent--corner {
    left: 0; top: 0;
    width: 150px; height: 60px;
    background: linear-gradient(135deg, var(--brand-yellow) 0%, var(--brand-yellow) 55%, rgba(255, 230, 0, 0) 100%);
  }
  .accent--base {
    left: 0; bottom: 0;
    width: 100%; height: 62px;
    background: linear-gradient(90deg, var(--brand-black) 0%, #3a3a20 35%, var(--brand-yellow) 70%, var(--brand-yellow) 100%);
  }

  .portrait {
    position: absolute;
    left: 448px; top: 122px;
    width: 391px; height: 359px;
    background: linear-gradient(180deg, var(--photo-mid) 0%, #6d5e55 40%, var(--photo-dark) 62%, #1f2633 100%);
    border-radius: 170px 170px 0 0;
  }

  .brand {
    position: absolute;
    display: flex;
    align-items: center;
    gap: 16px;
    font-family: "Pinyon Script", cursive;
    color: var(--ink);
    white-space: nowrap;
  }
  .brand__mark { background: var(--brand-yellow); width: 22px; height: 22px; }
  .brand--front { left: 133px; top: 78px; font-size: 38px; }
  .brand--back { left: 0; right: 0; top: 202px; justify-content: center; font-size: 54px; }
  .brand--back .brand__mark { background: var(--ink); width: 28px; height: 28px; }

  .holder-name {
    position: absolute;
    left: 66px; top: 210px;
    font-family: "Pinyon Script", cursive;
    font-size: 46px;
    color: var(--ink);
    white-space: nowrap;
  }

  .contact {
    position: absolute;
    left: 66px;
    list-style: none;
    font-family: "Source Sans 3", sans-serif;
    font-size: 20px;
    color: var(--ink-soft);
  }
  .contact--list { top: 292px; }
  .contact__item { display: flex; align-items: center; gap: 10px; height: 44px; }
  .contact__icon { width: 16px; height: 16px; fill: var(--ink-soft); }

  .tagline {
    position: absolute;
    left: 0; right: 0; top: 400px;
    text-align: center;
    font-family: "Questrial", sans-serif;
    font-size: 35px;
    letter-spacing: 0.5px;
    color: var(--ink);
  }
</style>
</head>
<body>

<section class="card card--front">
  <div class="accent accent--corner" role="img" aria-label="Yellow and black decorative swoosh in the corner"></div>
  <div class="accent accent--base" role="img" aria-label="Yellow and black decorative swoosh along the lower edge"></div>
  <div class="portrait" role="img" aria-label="Photo of the property investor, background removed"></div>

  <div class="brand brand--front"><span class="brand__mark"></span>Bright Door Homes</div>

  <div class="holder-name">Derek Pallister</div>

  <ul class="contact contact--list">
    <li class="contact__item">
      <svg class="contact__icon" viewBox="0 0 16 16" aria-hidden="true"><path d="M4 1 L6 1 L7 5 L5 6.5 C6 9 7 10 9.5 11 L11 9 L15 10 L15 12 C15 14 13 15 11 15 C6 14 2 10 1 5 C1 3 2 1 4 1 Z"/></svg>
      07845619027
    </li>
    <li class="contact__item">
      <svg class="contact__icon" viewBox="0 0 16 16" aria-hidden="true"><path d="M1 6 L8 1 L15 6 V14 H1 Z"/><path d="M2 7 L8 11 L14 7" fill="none" stroke="#e6e6e6" stroke-width="1.2"/></svg>
      brightdoorhomes@mailbox.example
    </li>
  </ul>
</section>

<section class="card card--back">
  <div class="brand brand--back"><span class="brand__mark"></span>Bright Door Homes</div>
  <p class="tagline">Need a quick sale? Let me help</p>
</section>

</body>
</html>
```